SLA & Internet Advert

Advertise some of our key SLA services & Internet Connectivity services.
Service Level Agreement:
Unlimited Remote, Email, Helpdesk & Telephone Support.
Unlimited Service Calls
Support Hours Monday - Saturday 7am-10pm Sunday till 5pm
Free additional visits during ofsted periods
Free remote access to school server for staff members
Free mobile device management for tablet devices
Free Email&Webhosting Service
Remote support on every device in school allowing us to close 90% of tickets within 30 mins.
Service Level Agreement Package 1 - Includes all the above + 1 Site visit every 2 weeks £2,500 per annum
Service Level Agreement Package 2 - Includes all the above + 1 Site Visit every week £4,500 per annum
Service Level Agreement Package 3 - Includes all the above + 2 Site visits every week - £7,540 per annum
Internet Connectivity (medium/large Primary)
Managed Firewall
Managed Web filter & Safeguarding
User reporting portal/email reporting.
Main Internet Line 1000 mb/s download 100mb/s upload
Back up Internet Line 80mb/s download 20mb/s upload
100% uptime guaranteed.
£3000 per annum
Internet Connectivity (Small Primary School)
Managed Firewall
£2100 per annum
My website is https://www.kolvarnet.co.uk if you need any further information like phone numbers / email address etc
Target Market(s)
Education
Look and feel
Each slider illustrates characteristics of the customer's brand and the style your logo design should communicate.

```html
<!DOCTYPE html>
<html lang="en">
<head>
<meta charset="utf-8">
<title>Kolvarnet SLA &amp; Internet Connectivity Flyer</title>
<link href="https://fonts.googleapis.com/css2?family=Montserrat:wght@400;500;600;700;800&display=swap" rel="stylesheet">
<style>
:root{
  --blue:#1b72c2;
  --orange:#ff5722;
  --dark:#222326;
  --paper:#f2f3f5;
  --ink:#2a2b2f;
  --stage:#c8cacd;
  --white:#ffffff;
}
*{margin:0;padding:0;box-sizing:border-box}
html,body{width:1200px;height:2289px;overflow:hidden}
body{background:var(--stage);font-family:"Montserrat",sans-serif;color:var(--ink);position:relative}
.flyer{position:absolute;left:80px;top:409px;width:882px;height:1248px;background:var(--paper);transform:scale(1.1791);transform-origin:0 0;overflow:hidden;box-shadow:0 10px 30px rgba(0,0,0,.18)}
.hero{position:absolute;left:0;top:0;width:882px;height:375px}
.hero svg{position:absolute;left:0;top:0}
.brand{position:absolute;left:26px;top:24px}
.brand-name{display:flex;align-items:center;gap:10px;font-weight:800;font-size:40px;color:var(--blue);letter-spacing:1px;line-height:1}
.brand-mark{width:26px;height:26px;background:var(--blue);display:inline-block}
.brand-tag{margin-top:10px;font-size:12.5px;font-weight:600;color:var(--blue);letter-spacing:.6px;border-top:1.5px solid var(--orange);padding-top:3px}
.hero-title{position:absolute;left:24px;top:143px;color:var(--white);font-weight:700;font-size:35px;line-height:44px}
.hero-rule{position:absolute;left:26px;top:286px;width:376px;height:3px;background:var(--blue)}
.hero-rule::after{content:"";position:absolute;left:19px;top:-1px;width:52px;height:5px;background:var(--orange);border-radius:3px}
.hero-sub{position:absolute;left:26px;top:307px;color:var(--white);font-size:18px;line-height:24px;font-weight:500}
.hero-sub b{font-weight:700}
.section-bar{position:absolute;left:26px;top:402px;width:829px;height:34px;display:flex;gap:7px}
.section-bar .accent{width:157px;background:var(--orange);border-radius:4px}
.section-bar .label{flex:1;background:var(--blue);border-radius:4px;color:var(--white);font-size:17px;display:flex;align-items:center;justify-content:center;letter-spacing:.3px}
.section-bar .label b{font-weight:700;margin:0 5px}
.list{position:absolute;list-style:none;font-size:14.5px;line-height:18px}
.list li{position:relative;padding-left:17px;margin-bottom:6px}
.list li::before{content:"";position:absolute;left:0;top:5px;width:6px;height:6px;background:var(--blue)}
.list b{font-weight:700}
.cards{position:absolute;left:26px;top:598px;display:flex;gap:17px}
.card{position:relative;width:265px;height:207px}
.card-tab{position:absolute;left:0;top:0;width:232px;height:24px;background:var(--orange);color:var(--white);font-size:14.5px;font-weight:500;padding-left:16px;line-height:24px;border-radius:4px 4px 0 0;z-index:2}
.card-body{position:absolute;left:0;top:12px;width:265px;height:195px;background:var(--blue);border-radius:0 18px 0 18px;color:var(--white);padding:22px 16px 0}
.card-title{font-size:21px;font-weight:700}
.card-desc{font-size:14.5px;font-weight:600;line-height:20px;margin-top:12px}
.card-price{font-size:34px;font-weight:700;margin-top:8px;line-height:40px}
.card-unit{display:inline-block;background:var(--orange);font-size:14.5px;font-weight:600;padding:2px 11px;border-radius:3px;margin-top:6px}
.net-head{position:absolute;top:832px;width:401px;height:56px;background:var(--orange);color:var(--white);border-radius:14px 0 14px 0;padding:8px 16px;font-size:14.5px;line-height:19px}
.net-head b{font-size:17px;font-weight:700;letter-spacing:.3px}
.remote-note{position:absolute;left:454px;top:1060px;font-size:14.5px;line-height:19px;color:var(--orange);font-weight:500}
.remote-note .hl{color:var(--blue);font-weight:700}
.remote-note sup{color:var(--blue);font-size:16px}
.contact-band{position:absolute;left:0;top:1120px;width:882px;height:66px;background:var(--blue);border-radius:28px 28px 0 0;display:flex;align-items:center;padding:0 26px;color:var(--white);font-size:14.5px}
.contact-btn{background:var(--orange);font-weight:700;font-size:16px;padding:5px 17px;border-radius:4px;margin-right:33px}
.contact-item{display:flex;align-items:center;gap:9px}
.contact-item b{font-weight:700}
.contact-sep{width:1.5px;height:28px;background:var(--white);margin:0 23px}
.footer{position:absolute;left:0;top:1186px;width:882px;height:62px;background:var(--dark);color:var(--white);display:flex;align-items:center;justify-content:center;font-size:14px;gap:10px}
.footer .dash{width:28px;height:1.5px;background:var(--white)}
.footer b{font-weight:700}
</style>
</head>
<body>
<main class="flyer">
  <header class="hero">
    <svg width="882" height="375" viewBox="0 0 882 375">
      <defs>
        <linearGradient id="photoTone" x1="0" y1="0" x2="1" y2="1">
          <stop offset="0" stop-color="#7a93a8"/>
          <stop offset=".5" stop-color="#8a5a52"/>
          <stop offset="1" stop-color="#4f5f6e"/>
        </linearGradient>
      </defs>
      <rect x="0" y="0" width="882" height="375" fill="url(#photoTone)" role="img" aria-label="Photo of a student wearing a virtual reality headset in a classroom"/>
      <polygon points="0,0 360,0 392,122 0,122" fill="var(--white)"/>
      <path d="M0,122 L392,122 L432,375 L34,375 Q0,375 0,341 Z" fill="var(--dark)"/>
      <polygon points="852,0 882,0 882,78" fill="var(--orange)"/>
    </svg>
    <div class="brand">
      <div class="brand-name"><span class="brand-mark"></span>KOLVARNET</div>
      <div class="brand-tag">EDUCATION SUPPORT &amp; INSTALLATION</div>
    </div>
    <h1 class="hero-title">Education, Support<br>and Installation of<br>all Technologies</h1>
    <div class="hero-rule"></div>
    <p class="hero-sub">We offer <b>fast, flexible, reliable</b> and<br><b>cost-effective</b> ICT support for <b>Education</b></p>
  </header>

  <div class="section-bar">
    <span class="accent"></span>
    <span class="label">OUR <b>SLA &amp; INTERNET CONNECTIVITY</b> SERVICES</span>
    <span class="accent"></span>
  </div>

  <ul class="list" style="left:26px;top:450px;width:410px">
    <li>Unlimited Remote, Email, Helpdesk and Telephone Support.</li>
    <li>Support Hours<br>Monday - Saturday <b>7am-10pm</b>, Sunday till <b>5pm</b></li>
    <li>Unlimited Service Calls</li>
    <li>Free Email &amp; Webhosting Service</li>
  </ul>
  <ul class="list" style="left:454px;top:450px;width:400px">
    <li>Free additional visits during ofsted periods</li>
    <li>Free remote access to school server<br>for staff members</li>
    <li>Free mobile device management for<br>tablet devices</li>
  </ul>

  <section class="cards">
    <article class="card">
      <div class="card-tab">Service Level Agreement</div>
      <div class="card-body">
        <div class="card-title">Package 1 -</div>
        <div class="card-desc">Includes all the above +<br>1 Site visit every 2 weeks</div>
        <div class="card-price">£2,500</div>
        <span class="card-unit">Per Annum</span>
      </div>
    </article>
    <article class="card">
      <div class="card-tab">Service Level Agreement</div>
      <div class="card-body">
        <div class="card-title">Package 2 -</div>
        <div class="card-desc">Includes all the above +<br>1 Site visit every weeks</div>
        <div class="card-price">£4,500</div>
        <span class="card-unit">Per Annum</span>
      </div>
    </article>
    <article class="card">
      <div class="card-tab">Service Level Agreement</div>
      <div class="card-body">
        <div class="card-title">Package 3 -</div>
        <div class="card-desc">Includes all the above +<br>2 Site visit every weeks</div>
        <div class="card-price">£7,540</div>
        <span class="card-unit">Per Annum</span>
      </div>
    </article>
  </section>

  <div class="net-head" style="left:26px">Internet Connectivity<br><b>(MEDIUM/LARGE PRIMARY)</b></div>
  <div class="net-head" style="left:454px">Internet Connectivity<br><b>(SMALL PRIMARY SCHOOL)</b></div>

  <ul class="list" style="left:26px;top:900px;width:410px">
    <li>Managed Firewall</li>
    <li>Managed Web filter &amp; Safeguarding</li>
    <li>User reporting portal / email reporting.</li>
    <li>Main Internet Line <b>1000 mb/s</b> download<br><b>100mb/s</b> upload</li>
    <li>Back up Internet Line <b>80mb/s</b> download<br><b>20mb/s</b> upload</li>
    <li><b>100%</b> uptime guaranteed.</li>
    <li><b>£3000</b> per annum</li>
  </ul>
  <ul class="list" style="left:454px;top:900px;width:410px">
    <li>Managed Firewall</li>
    <li>Managed Web filter &amp; Safeguarding</li>
    <li>User reporting portal / email reporting.</li>
    <li>Main Internet Line <b>1000 mb/s</b> download<br><b>100mb/s</b> upload</li>
    <li><b>£2100</b> per annum</li>
  </ul>

  <p class="remote-note"><span class="hl">Remote Support</span> on every device in school<sup>*</sup><br>allowing us to close <span class="hl">90%</span> of tickets within <span class="hl">30 mins</span>.</p>

  <footer>
    <div class="contact-band">
      <span class="contact-btn">CONTACT US</span>
      <span class="contact-item">
        <svg width="24" height="24" viewBox="0 0 24 24" aria-hidden="true"><circle cx="12" cy="12" r="11" fill="none" stroke="#fff" stroke-width="1.5"/><path d="M8.5 6.5l2 2.3-1.2 1.4c.8 1.7 2 2.9 3.6 3.7l1.4-1.2 2.3 2-1.2 1.9c-3.9-.4-7.6-4.1-8-8z" fill="var(--orange)"/></svg>
        <b>0161 555 0147</b>
      </span>
      <span class="contact-sep"></span>
      <span class="contact-item">
        <svg width="24" height="24" viewBox="0 0 24 24" aria-hidden="true"><circle cx="12" cy="12" r="11" fill="none" stroke="#fff" stroke-width="1.5"/><g fill="none" stroke="var(--orange)" stroke-width="1.4"><circle cx="12" cy="12" r="6"/><ellipse cx="12" cy="12" rx="2.6" ry="6"/><path d="M6 12h12"/></g></svg>
        <span>www.<b>kolvarnet</b>.co.uk</span>
      </span>
      <span class="contact-sep"></span>
      <span class="contact-item">
        <svg width="24" height="24" viewBox="0 0 24 24" aria-hidden="true"><circle cx="12" cy="12" r="11" fill="none" stroke="#fff" stroke-width="1.5"/><g fill="none" stroke="var(--orange)" stroke-width="1.4"><rect x="6.5" y="8" width="11" height="8" rx="1"/><path d="M6.5 8.5l5.5 4 5.5-4"/></g></svg>
        <span>info@<b>kolvarnet</b>.co.uk</span>
      </span>
    </div>
    <div class="footer">
      <span class="dash"></span>
      <span>Kolvarnet LTD <b>Northgate House, Kelso Street Bury Lancashire</b> BL9 0ZZ</span>
      <span class="dash"></span>
    </div>
  </footer>
</main>
</body>
</html>
```